Capability Statement Document/Flyer

Take the existing words from the capability statement document (attached) and design a unique folder/flyer document for professional use. Maybe something like a trifold or bifold style. Use approved colours and logo as per the attached files.
Our company designs and builds small onshore gas processing plants.

```html
<!DOCTYPE html>
<html lang="en">
<head>
<meta charset="utf-8">
<title>Clarivo Capability Statement</title>
<link href="https://fonts.googleapis.com/css2?family=Montserrat:wght@400;500;600;700;800&display=swap" rel="stylesheet">
<style>
:root{
  --green:#15806a;
  --green-dark:#0d5f4f;
  --green-mid:#1b7563;
  --grey:#bdbdbd;
  --grey-light:#f1f1f1;
  --grey-row:#e9e9e9;
  --ink:#3a3a3a;
  --bg:#e6e8e7;
  --white:#ffffff;
}
*{box-sizing:border-box;margin:0;padding:0}
html,body{width:1200px;height:590px;overflow:hidden;background:var(--bg);font-family:"Montserrat",sans-serif;color:var(--ink)}
.canvas{position:relative;width:1200px;height:590px}
.spread{position:absolute;top:90px;width:760px;height:537px;background:var(--white);transform:scale(.763);transform-origin:0 0;overflow:hidden;box-shadow:0 2px 8px rgba(0,0,0,.15)}
.spread--outside{left:10px}
.spread--inside{left:610px}
.abs{position:absolute}
h3{font-size:13px;font-weight:700;color:var(--green)}
.list{list-style:none;margin-top:8px}
.list li{position:relative;font-size:6.6px;line-height:1.25;padding-left:12px;margin-bottom:3px}
.list li::before{position:absolute;left:0;top:0;width:8px;height:8px;border-radius:50%;background:var(--green);color:#fff;font-size:6px;line-height:8px;text-align:center;font-weight:700}
.list--ticks li::before{content:"✓"}
.list--crosses li::before{content:"✕";background:#fff;border:1px solid var(--green);color:var(--green);line-height:6px;font-size:5.5px}
.contact-tab{left:200px;top:112px;width:178px;height:35px;background:var(--green);clip-path:polygon(0 0,100% 0,100% 100%,12% 100%);color:#fff;padding:5px 0 0 26px}
.contact-tab b{display:block;font-size:7.4px;font-weight:700}
.contact-tab span{font-size:6.6px}
.person{left:16px;width:346px}
.person .row{display:grid;height:20px;background:var(--green);color:#fff;font-size:7.4px;font-weight:600;align-items:center;margin-bottom:2px}
.person .row > div{height:100%;display:flex;align-items:center;padding-left:6px;border-right:1.5px solid #fff}
.person .row > div:last-child{border-right:0}
.row--name{grid-template-columns:60px 90px 60px 1fr}
.row--exp{grid-template-columns:60px 1fr}
.row--exp .lbl{background:var(--green-dark);font-weight:700}
.row--exp .val{font-weight:500;font-size:6.6px;line-height:1.15}
.person p{font-size:5.8px;line-height:1.25;padding:4px 6px 0;color:#555}
.photo{background:linear-gradient(160deg,#a9c3d6 0%,#c9d2cf 35%,#8f9a98 60%,#d9c98a 100%)}
.photo--cool{background:linear-gradient(180deg,#7ea6c6 0%,#c8d4da 40%,#6f8f8c 75%,#2d6e6a 100%)}
.logo-box{left:400px;top:17px;width:187px;height:48px;background:#fff;border:3px solid #7a7a7a;display:flex;align-items:center;justify-content:center;font-size:34px;font-weight:700;color:var(--green);letter-spacing:1px}
.title-box{left:378px;top:297px;width:280px;height:78px;background:var(--green);clip-path:polygon(0 0,82% 0,100% 100%,0 100%);color:#fff;font-size:29px;font-weight:800;line-height:1;padding:10px 0 0 18px}
.tagline{left:396px;top:390px;font-size:10.5px;font-weight:500;color:#333;line-height:1.25}
.contacts{left:396px;top:465px;font-size:7px;line-height:1.45;color:#333}
.contacts div{display:flex;gap:6px;align-items:flex-start}
.contacts svg{flex:none;margin-top:1px}
.para{font-size:7px;line-height:1.3}
.vision{font-size:7.6px;font-weight:700;color:var(--green);margin:8px 0 6px}
.principles{font-size:7px;line-height:1.55}
.principles b{color:var(--green)}
.hex-label{font-size:7.6px;font-weight:700;fill:#333;font-family:"Montserrat",sans-serif}
.node-label{font-size:7px;font-weight:700;fill:var(--green);font-family:"Montserrat",sans-serif}
.heading-rule{display:flex;align-items:center;gap:8px}
.heading-rule::after{content:"";flex:1;height:8px;background:var(--grey-light)}
.table{width:100%;font-size:6.6px}
.table .tr{display:grid;align-items:center;border-bottom:1px solid #fff}
.table .th{background:var(--green);color:#fff;font-weight:700;font-size:7.4px;height:18px}
.table .tr > div{padding-left:8px}
.services .tr{grid-template-columns:30px 122px 1fr}
.services .td{height:24px;background:#fff;border-bottom:1px solid #e4e4e4}
.services .td > div:first-child{text-align:center;padding-left:0}
.services .td > div:nth-child(2){font-weight:600;background:var(--grey-light);height:100%;display:flex;align-items:center}
.services .td > div:last-child{font-size:5.6px;line-height:1.2}
.services .td > div:first-child{background:var(--grey-light);height:100%;display:flex;align-items:center;justify-content:center}
.roles .tr{grid-template-columns:1fr 1fr}
.roles .td{height:20.5px;background:var(--grey-row);font-weight:600;font-size:6.8px}
.roles .td:nth-child(odd){background:#f6f6f6}
.objective{left:0;top:458px;width:378px;height:79px;background:#d8d8d8;clip-path:polygon(0 0,86% 0,100% 100%,0 100%)}
.objective h3{position:absolute;left:18px;top:10px;font-size:12px}
.objective p{position:absolute;left:18px;top:35px;width:310px;font-size:6.4px;line-height:1.3}
.placeholder{background:linear-gradient(180deg,#d9dcdb,#bfc4c2)}
</style>
</head>
<body>
<main class="canvas">

  <!-- OUTSIDE SPREAD -->
  <section class="spread spread--outside">
    <div class="abs" style="left:16px;top:14px;width:176px">
      <h3>PDP Benefits:</h3>
      <ul class="list list--ticks">
        <li>Provides owners with access to experienced project delivery capability</li>
        <li>Improved project controls and governance</li>
        <li>Greater flexibility than traditional EPC delivery</li>
        <li>Enhanced visibility and management of cost, schedule and risk</li>
        <li>Scalable resources aligned with project phases</li>
      </ul>
    </div>
    <div class="abs" style="left:210px;top:14px;width:165px">
      <h3>PDP Challenges:</h3>
      <ul class="list list--crosses">
        <li>Owner retains significant delivery risk</li>
        <li>Requires clear governance and decision-making processes</li>
        <li>Multiple contractor interfaces require strong coordination</li>
        <li>Success depends on collaborative Owner-PDP relationship</li>
      </ul>
    </div>
    <svg class="abs" style="left:0;top:0" width="378" height="160" aria-hidden="true">
      <line x1="0" y1="133" x2="203" y2="133" stroke="var(--green)" stroke-width="2"/>
    </svg>
    <div class="abs contact-tab"><b>For More Information Contact:</b><span>directors@clarivo.com.au</span></div>

    <h3 class="abs" style="left:16px;top:147px">Key Clarivo Personnel</h3>

    <div class="abs person" style="top:177px">
      <div class="row row--name"><div>Name:</div><div>Owen Hartley</div><div>Role:</div><div>Executive Director</div></div>
      <div class="row row--exp"><div class="lbl">35yrs Exp:</div><div class="val">Harbourline, Northreach Energy, KTVS, Meridian Gas</div></div>
      <p>Extensive global energy industry experience, from frontline O&amp;M to the boardroom. Respected 'C Suite' leader with a track record of building high performing teams that deliver outstanding results.</p>
    </div>
    <div class="abs person" style="top:258px">
      <div class="row row--name"><div>Name:</div><div>Neil Castell</div><div>Role:</div><div>Technical Director</div></div>
      <div class="row row--exp" style="height:24px"><div class="lbl">39yrs Exp:</div><div class="val">Harbourline, Northreach Energy, Gulfstone Petroleum,<br>Corvane, Ardent Group, Eastfield Gas, KTVS, Meridian Gas</div></div>
      <p>Highly skilled &amp; experienced operations &amp; project management professional with 39 years' experience in the global oil &amp; gas industry delivering multiple projects and establishing best in class operational assets. Deep knowledge of project management, construction, commissioning &amp; start-up including a global functional assurance role.</p>
    </div>
    <div class="abs person" style="top:353px">
      <div class="row row--name"><div>Name:</div><div>Dean Whitford</div><div>Role:</div><div>Commercial Director</div></div>
      <div class="row row--exp"><div class="lbl">40yrs Exp:</div><div class="val">Westmere, Tarrow, Corvane, KTVS, Meridian Gas</div></div>
      <p>Senior Logistics &amp; Supply Chain Manager / Procurement Manager with strong operational, commercial, project management, negotiating &amp; relationship building skills. Experienced in operating complex and diverse logistics operations, significantly improving service levels whilst reducing cost.</p>
    </div>
    <div class="abs person" style="top:441px">
      <div class="row row--name"><div>Name:</div><div>Ross Calder</div><div>Role:</div><div>Operations Director</div></div>
      <div class="row row--exp"><div class="lbl">27yrs Exp:</div><div class="val">Corvane, Ardent Group, Eastfield Gas, KTVS, Meridian Gas</div></div>
      <p>27 years' success leading operations, maintenance and commissioning teams on onshore and offshore oil and gas production platforms, FPSOs, gas processing, coal seam gas, refrigeration facilities, and chemical refineries. Results driven and enthusiastic leader with a proven track record of delivery.</p>
    </div>

    <!-- cover panel -->
    <div class="abs photo" role="img" aria-label="Photograph of an onshore gas processing plant with pipework and vessels" style="left:378px;top:0;width:382px;height:282px"></div>
    <div class="abs" style="left:378px;top:0;width:382px;height:282px;background:var(--green);clip-path:polygon(66% 0,100% 0,100% 40%)"></div>
    <div class="abs logo-box">CLARIVO</div>
    <div class="abs" style="left:378px;top:280px;width:382px;height:257px;background:#fff"></div>
    <div class="abs photo--cool" role="img" aria-label="Photograph of plant piping and a flare stack" style="left:378px;top:280px;width:382px;height:257px;clip-path:polygon(62% 0,100% 0,100% 100%,58% 100%,72% 55%)"></div>
    <div class="abs" style="left:378px;top:280px;width:290px;height:200px;background:var(--grey);clip-path:polygon(0 0,63% 0,95% 48%,70% 100%,0 100%)"></div>
    <svg class="abs" style="left:378px;top:280px" width="382" height="257" aria-hidden="true">
      <polygon points="190,200 204,200 250,257 236,257" fill="var(--green)"/>
    </svg>
    <div class="abs title-box">CAPABILITY<br>STATEMENT</div>
    <div class="abs tagline">Simplify Project Execution,<br>Streamline Operations</div>
    <div class="abs contacts">
      <div><svg width="7" height="7" viewBox="0 0 10 10"><path d="M2 0l2 2.5-1.2 1.2a6 6 0 003.5 3.5L7.5 6 10 8 8.5 10C4 9.5.5 6 0 1.5z" fill="var(--green)"/></svg>+00 1000 200 3000</div>
      <div><svg width="7" height="7" viewBox="0 0 10 10"><rect x="0" y="2" width="10" height="6.5" fill="var(--green)"/><path d="M0 2l5 3.5L10 2" stroke="#fff" fill="none"/></svg>directors@clarivo.com.au</div>
      <div><svg width="7" height="7" viewBox="0 0 10 10"><circle cx="5" cy="5" r="4.3" fill="none" stroke="var(--green)" stroke-width="1.4"/><line x1=".8" y1="5" x2="9.2" y2="5" stroke="var(--green)"/></svg>www.clarivo.com.au</div>
      <div><svg width="7" height="8" viewBox="0 0 10 12"><path d="M5 0a4 4 0 014 4c0 3-4 8-4 8S1 7 1 4a4 4 0 014-4z" fill="var(--green)"/><circle cx="5" cy="4" r="1.4" fill="#fff"/></svg>45 Harbour Rd, Level 8, Perth,<br>Western Australia 6000, AU</div>
    </div>
  </section>

  <!-- INSIDE SPREAD -->
  <section class="spread spread--inside">
    <div class="abs photo--cool" role="img" aria-label="Photograph of a tall gas processing column" style="left:0;top:0;width:135px;height:245px"></div>
    <div class="abs" style="left:132px;top:14px;width:235px">
      <h3>Who are Clarivo?</h3>
      <p class="para" style="margin-top:8px">Clarivo are a highly experienced team of Executive, Project, Construction, Commissioning and Operations specialists who combine deep technical knowledge with proven leadership to deliver unique Project Delivery Partner services to organisations in Australia.</p>
      <p class="vision">Our vision is straightforward:</p>
      <p class="para">Simplify Project Execution, Streamline Operations.</p>
      <h3 style="margin-top:14px;line-height:1.25">What is a Project Delivery<br>Partner?</h3>
      <p class="para" style="margin-top:8px">A Project Delivery Partner (PDP) provides integrated project management along with technical, commercial and delivery support services to help an organisation successfully deliver a project. The PDP acts as the owner's team while the owner retains accountability and key decision-making authority.</p>
    </div>

    <div class="abs" style="left:0;top:245px;width:378px;height:292px;background:var(--grey-light)"></div>
    <div class="abs" style="left:18px;top:258px;width:200px">
      <h3>PDP Core Principles:</h3>
      <p class="principles" style="margin-top:8px"><b>1.</b> Owner controls the project<br><b>2.</b> PDP enables delivery &amp; provides assurance<br><b>3.</b> Contractors execute the work</p>
    </div>
    <svg class="abs" style="left:0;top:245px" width="378" height="213" aria-hidden="true">
      <g fill="var(--grey)" stroke="#fff" stroke-width="2">
        <polygon points="64,102 74,85 94,85 104,102 94,119 74,119"/>
        <polygon points="142,102 152,85 172,85 182,102 172,119 152,119"/>
        <polygon points="217,50 227,33 247,33 257,50 247,67 227,67"/>
        <polygon points="217,102 227,85 247,85 257,102 247,119 227,119"/>
        <polygon points="217,154 227,137 247,137 257,154 247,171 227,171"/>
      </g>
      <text class="hex-label" x="84" y="100" text-anchor="middle">Operator</text>
      <text class="hex-label" x="84" y="109" text-anchor="middle">XYZ</text>
      <text class="hex-label" x="162" y="105" text-anchor="middle">Clarivo</text>
      <text class="hex-label" x="237" y="53" text-anchor="middle">Engineering</text>
      <text class="hex-label" x="237" y="105" text-anchor="middle">Suppliers</text>
      <text class="hex-label" x="237" y="157" text-anchor="middle">Execution</text>
      <g stroke="var(--green)" stroke-width="1" fill="none">
        <line x1="84" y1="121" x2="84" y2="131"/><path d="M81 128l3 3 3-3"/>
        <line x1="162" y1="121" x2="162" y2="131"/><path d="M159 128l3 3 3-3"/>
        <line x1="237" y1="173" x2="237" y2="183"/><path d="M234 180l3 3 3-3"/>
      </g>
      <text class="node-label" x="84" y="142" text-anchor="middle">Owner</text>
      <text class="node-label" x="162" y="142" text-anchor="middle">Project</text>
      <text class="node-label" x="162" y="151" text-anchor="middle">Delivery</text>
      <text class="node-label" x="162" y="160" text-anchor="middle">Partner</text>
      <text class="node-label" x="237" y="194" text-anchor="middle">Contractors</text>
      <line x1="112" y1="183" x2="140" y2="183" stroke="var(--green)" stroke-dasharray="2 2"/>
    </svg>
    <div class="abs placeholder" role="img" aria-label="Illustration of a business figure with a briefcase" style="left:18px;top:360px;width:40px;height:95px;border-radius:6px"></div>
    <div class="abs placeholder" role="img" aria-label="Illustration of two business figures with briefcases" style="left:272px;top:268px;width:100px;height:185px;border-radius:8px"></div>

    <div class="abs objective">
      <h3>PDP Objective:</h3>
      <p>Deliver the project safely, on schedule, within budget and ready for operations; providing owner capability throughout the project lifecycle.</p>
    </div>
    <svg class="abs" style="left:0;top:458px" width="378" height="79" aria-hidden="true">
      <polygon points="326,60 350,60 362,79 338,79" fill="var(--green)"/>
    </svg>

    <div class="abs" style="left:395px;top:14px;width:348px">
      <h3 class="heading-rule">PDP Services:</h3>
      <div class="table services" style="margin-top:10px">
        <div class="tr th"><div style="text-align:center;padding-left:0">#</div><div>Function</div><div>Clarivo Service</div></div>
        <div class="tr td"><div>1</div><div>Project Management</div><div>Planning, Reporting &amp; Delivery Leadership<br>from Concept to Completion</div></div>
        <div class="tr td"><div>2</div><div>Engineering</div><div>Concept Selection, Design Coordination,<br>Technical Assurance &amp; Value Engineering</div></div>
        <div class="tr td"><div>3</div><div>Procurement</div><div>Contracting Strategy, Tender Process &amp;<br>Supplier/Contractor Management</div></div>
        <div class="tr td"><div>4</div><div>Approvals</div><div>Land Access, Regulator Engagement,<br>Safety Case, Permits &amp; Licenses</div></div>
        <div class="tr td"><div>5</div><div>Cost Control</div><div>Budget Development,<br>Forecasting &amp; Management</div></div>
        <div class="tr td"><div>6</div><div>Scheduling</div><div>Master Schedule Development, WBS,<br>Resource Allocation, Monitoring &amp; Updating</div></div>
        <div class="tr td"><div>7</div><div>Risk Management</div><div>Risk Register, Identification,<br>Mitigation &amp; Reporting</div></div>
        <div class="tr td"><div>8</div><div>Governance</div><div>Framework, Stage Gates, Change control,<br>Reporting &amp; Decision Support</div></div>
        <div class="tr td"><div>9</div><div>Construction</div><div>Management &amp; Coordination of<br>Contractor Execution Teams</div></div>
        <div class="tr td"><div>10</div><div>Commissioning &amp; Start-up</div><div>Lead Commissioning &amp; Start-up, Completions System,<br>Bring the Facility to Steady-State</div></div>
        <div class="tr td"><div>11</div><div>Operations Readiness</div><div>People &amp; Organisation, Process &amp; Procedures,<br>Systems &amp; Technology</div></div>
        <div class="tr td"><div>12</div><div>Operations &amp; Maintenance</div><div>Monitor &amp; Operate Asset, Minimize Downtime,<br>Lowest Possible OPEX for Owner</div></div>
      </div>
      <h3 class="heading-rule" style="margin-top:20px">PDP Roles &amp; Responsibilities:</h3>
      <div class="table roles" style="margin-top:12px">
        <div class="tr th"><div>Owner</div><div>Clarivo Service</div></div>
        <div class="tr td"><div>Sets Project Objectives</div><div>Develops Delivery Plans</div></div>
        <div class="tr td"><div>Approves Major Decisions</div><div>Provides Recommendations</div></div>
        <div class="tr td"><div>Holds Project Risk</div><div>Identifies and Manages Risks</div></div>
        <div class="tr td"><div>Awards Contracts</div><div>Manages Contractor Interfaces</div></div>
        <div class="tr td"><div>Provides Funding</div><div>Monitors Cost and Schedule Performance</div></div>
      </div>
    </div>
  </section>

</main>
</body>
</html>
```